We specialize in pizza, pasta and salads and are now offering TAKE & BAKE and GRAB & GO ...

Looking for either a 8.5" x 11" or similar for a instore display. WILL BE ON A SWIVELING HOLDER to catch customers attention.

**THIS IS A DOUBLE SIDED PRINT**

ONE SIDE will consist of WHAT'S FOR DINNER TONIGHT? and the following:
* Take & Bake"
* "Baked Pasta"
* Freshly made in house
* Lasagna
$13.50
- please include attached closeup picture and logo

THE OTHER SIDE will consist of
mini charcutier board.
* snack size charcutier delight *
* Enjoy the flavors of gourmet snacking, all in one convenient box!

PRICE $8.99

Winning design will be commissioned to design labels for "grab and go" for take and bake pasta, charcuterie box, pasta salads, candy etc.

Thank you and please do not hesitate to ask any questions.

www.calderipizza.ca
www.fernloop.ca
Logo to be interchanged as they are affiliated meaning FernLoop is a brand within Calderi pizza.

Target Market(s)

our target market is customers who have already entered our business. This is to upsel

Industry/Entity Type

We are in a self serve enviroment and target business people

Requirements
Must have
• must be clean and catchy. We are located in a professional business community.
Nice to have
• Must be appealing, appetizing and utilize our website colors
Should not have
• should not have any carton drawings and not be cluttered (busy)

```html
<!DOCTYPE html>
<html lang="en">
<head>
<meta charset="utf-8">
<title>Calderi Pizza – Take &amp; Bake and Charcutier Board Display</title>
<link href="https://fonts.googleapis.com/css2?family=Alegreya+Sans+SC:wght@800;900&family=Kaushan+Script&family=Montserrat:wght@400;500&family=Oswald:wght@600&family=Yellowtail&display=swap" rel="stylesheet">
<style>
  :root {
    --stage: #c4c4c4;
    --wine-deep: #3a0307;
    --wine-mid: #7a0a10;
    --wine-glow: #b8161c;
    --white: #ffffff;
    --gold: #ffd21c;
    --orange: #f07a12;
    --amber: #ffb400;
    --price-ink: #8a0d10;
    --brand-ink: #3b3b3b;
  }
  * { margin: 0; padding: 0; box-sizing: border-box; }
  html, body { width: 1200px; height: 819px; overflow: hidden; background: var(--stage); }
  .canvas { position: relative; width: 1200px; height: 819px; }

  .flyer {
    position: absolute; top: 81px; width: 508px; height: 657px; overflow: hidden;
    background: radial-gradient(ellipse 70% 55% at 50% 45%, var(--wine-glow) 0%, var(--wine-mid) 50%, var(--wine-deep) 100%);
    box-shadow: 0 2px 8px rgba(0,0,0,.25);
  }
  .flyer--dinner { left: 82px; }
  .flyer--board { left: 610px; }
  .flyer > * { position: absolute; }

  .kicker { font-family: "Montserrat", sans-serif; font-weight: 500; color: var(--white); text-align: center; left: 0; right: 0; }
  .script-gold {
    font-family: "Kaushan Script", cursive; text-align: center; left: 0; right: 0;
    background: linear-gradient(90deg, var(--orange), var(--amber) 50%, var(--gold));
    -webkit-background-clip: text; background-clip: text; color: transparent; line-height: 1;
  }
  .display-caps { font-family: "Alegreya Sans SC", sans-serif; font-weight: 900; color: var(--white); line-height: 1; }
  .display-caps--gold { color: var(--gold); }

  .photo { border-radius: 50%; }

  .price-badge {
    width: 124px; height: 124px; border-radius: 50%;
    background: linear-gradient(180deg, var(--gold) 0%, var(--amber) 62%, #fff3c8 63%, #e8d9a8 100%);
    display: flex; align-items: center; justify-content: center;
    font-family: "Oswald", sans-serif; font-weight: 600; color: var(--price-ink); font-size: 40px;
  }
  .price-badge sup { font-size: 20px; vertical-align: 16px; }

  .footer { left: 0; right: 0; bottom: 0; height: 90px; background: var(--white); }
  .footer::before {
    content: ""; position: absolute; left: 0; right: 0; top: -10px; height: 10px;
    background: radial-gradient(circle at 50% 100%, var(--white) 11px, transparent 11.5px) repeat-x;
    background-size: 24px 10px;
  }
  .brand-main { position: absolute; font-family: "Montserrat", sans-serif; font-weight: 400; font-size: 26px; color: var(--brand-ink); letter-spacing: .5px; top: 24px; }
  .brand-sub { position: absolute; text-align: center; top: 6px; }
  .brand-sub .mark { display: block; width: 34px; height: 34px; border-radius: 50%; border: 2px solid #1f3a6b; margin: 0 auto 3px; }
  .brand-sub .name { font-family: "Montserrat", sans-serif; font-weight: 400; font-size: 15px; color: #1f3a6b; }
</style>
</head>
<body>
<main class="canvas">

  <!-- Front: take & bake lasagna -->
  <section class="flyer flyer--dinner">
    <p class="kicker" style="top:28px;font-size:25px;">WHAT'S FOR</p>
    <h1 class="script-gold" style="top:52px;font-size:50px;">Dinner tonight</h1>
    <h2 class="display-caps" style="top:134px;left:0;right:0;text-align:center;font-size:54px;letter-spacing:1px;">Take &amp; Bake</h2>
    <p class="display-caps" style="top:193px;left:56px;font-size:23px;text-align:center;">Freshly<br>made in house</p>

    <div class="photo-plate" role="img" aria-label="Slice of baked lasagna on a dark plate with basil and chili"
         style="left:86px;top:239px;width:256px;height:192px;border-radius:45%;background:radial-gradient(ellipse at 50% 40%, #e9b45a 0%, #c9782c 45%, #3a2520 75%, transparent 76%);"></div>

    <div class="photo" role="img" aria-label="Close-up of melted cheese pulling from baked pasta"
         style="left:328px;top:251px;width:160px;height:160px;border:6px solid var(--white);background:radial-gradient(circle at 45% 45%, #e3c48a, #8a5a22 60%, #2a1a10);"></div>

    <svg style="left:0;top:0;" width="508" height="657" viewBox="0 0 508 657" aria-hidden="true">
      <defs><path id="arc-pasta" d="M 318 300 A 96 96 0 0 1 505 318"/></defs>
      <text font-family="Alegreya Sans SC, sans-serif" font-weight="900" font-size="30" fill="#ffd21c">
        <textPath href="#arc-pasta">BAKED PASTA</textPath>
      </text>
    </svg>

    <div class="price-badge" style="left:14px;top:289px;"><sup>$</sup>13.50</div>

    <h2 style="left:0;right:0;top:410px;text-align:center;font-family:'Yellowtail',cursive;font-weight:400;font-size:100px;color:var(--white);line-height:1;">Lasagna</h2>

    <footer class="footer">
      <span class="brand-main" style="left:108px;">CALDERI PIZZA</span>
      <div class="brand-sub" style="left:304px;width:96px;"><span class="mark"></span><span class="name">FernLoop</span></div>
    </footer>
  </section>

  <!-- Back: mini charcutier board -->
  <section class="flyer flyer--board">
    <p class="kicker" style="top:38px;font-size:30px;">MINI</p>
    <h1 class="script-gold" style="top:52px;font-size:68px;">Charcutier</h1>
    <p style="left:0;right:0;top:104px;text-align:center;font-family:'Kaushan Script',cursive;font-size:46px;color:var(--white);line-height:1;">Board.</p>

    <h2 class="display-caps" style="top:170px;left:58px;width:130px;text-align:center;font-size:36px;">Snack<br>size</h2>
    <p class="display-caps display-caps--gold" style="top:241px;left:40px;width:170px;text-align:center;font-size:25px;">Charcutier<br>delight</p>

    <div role="img" aria-label="Wooden board with cured meats, cheeses, olives and sun-dried tomatoes"
         style="left:200px;top:208px;width:300px;height:280px;border-radius:24px;transform:rotate(-8deg);background:radial-gradient(ellipse at 45% 50%, #e9a3a0 0%, #b5484c 35%, #e8d9b0 60%, #c68a45 80%, transparent 81%);"></div>

    <div class="price-badge" style="left:334px;top:153px;"><sup>$</sup>8.99</div>

    <p class="display-caps" style="top:386px;left:52px;font-size:25px;line-height:1.0;">Enjoy the<br>flavors of<br>gourmet<br>snacking</p>
    <p class="script-gold" style="top:495px;font-size:30px;left:-30px;right:0;background:none;color:var(--gold);">All in one convenient box</p>

    <footer class="footer">
      <span class="brand-main" style="left:108px;">CALDERI PIZZA</span>
      <div class="brand-sub" style="left:316px;width:96px;top:10px;"><span class="mark"></span><span class="name">FernLoop</span></div>
    </footer>
  </section>

</main>
</body>
</html>
```